New Logo and Business Card

Want new logo and business card for multi brand website. Attached are the logos for the back of the card.
We want a new logo for the front, the name "Tallvane" as the company name.
The logo can just be an "T" and a "V" for simplicity. With the text "Tallvane" after it.
For the business card use this info:
Doran Pelliske, PEng MBA
President
doran.pelliske@tallvane-mail.ca
+14035558213
Industry/Entity Type
Business
Logo Text
Tallvane
Logo styles of interest
Lettermark Logo

```html
<!DOCTYPE html>
<html lang="en">
<head>
<meta charset="utf-8">
<title>Tallvane Business Card</title>
<link href="https://fonts.googleapis.com/css2?family=Tenor+Sans&family=Arimo:wght@400;700&display=swap" rel="stylesheet">
<style>
  :root {
    --backdrop: #2e2e2e;
    --card: #ffffff;
    --band: #4a4645;
    --accent: #ee7a1c;
    --ink: #1c1c1c;
    --ink-soft: #2a2a2a;
    --band-text: #ffffff;
  }
  * { margin: 0; padding: 0; box-sizing: border-box; }
  html, body {
    width: 1200px; height: 960px; overflow: hidden;
    background: var(--backdrop);
  }
  .stage { position: relative; width: 1200px; height: 960px; }
  .card {
    position: absolute; left: 326px; width: 531px; height: 326px;
    background: var(--card); overflow: hidden;
  }
  .card--front { top: 137px; }
  .card--back { top: 492px; }

  .band {
    position: absolute; background: var(--band);
    border-bottom: 4px solid var(--accent);
  }
  .band__name {
    position: absolute; left: 14px; top: 50%;
    transform: translateY(-52%);
    font-family: "Tenor Sans", sans-serif;
    color: var(--band-text);
    text-transform: uppercase; letter-spacing: 1px; white-space: nowrap;
  }
  .name-marker {
    position: absolute; background: var(--band);
  }

  /* front */
  .card--front .band--stub { left: 0; top: 132px; width: 34px; height: 66px; }
  .card--front .band--main { left: 202px; top: 130px; width: 329px; height: 70px; }
  .card--front .band__name { font-size: 34px; }
  .card--front .name-marker { left: 166px; top: 149px; width: 26px; height: 26px; }

  /* back */
  .card--back .band--stub { left: 0; top: 45px; width: 34px; height: 46px; }
  .card--back .band--main { left: 309px; top: 43px; width: 222px; height: 50px; }
  .card--back .band__name { font-size: 24px; left: 10px; }
  .card--back .name-marker { left: 283px; top: 56px; width: 18px; height: 18px; }

  .contact {
    position: absolute; left: 0; right: 0; top: 152px;
    text-align: center; font-family: "Arimo", sans-serif; color: var(--ink-soft);
  }
  .contact__name { font-size: 27px; font-weight: 700; color: var(--ink); line-height: 1.15; }
  .contact__role { font-size: 17px; line-height: 1.2; }
  .contact__lines { margin-top: 20px; font-size: 17px; line-height: 1.4; }
</style>
</head>
<body>
<main class="stage">
  <section class="card card--front">
    <div class="band band--stub"></div>
    <div class="name-marker"></div>
    <div class="band band--main"><span class="band__name">Tallvane</span></div>
  </section>

  <section class="card card--back">
    <div class="band band--stub"></div>
    <div class="name-marker"></div>
    <div class="band band--main"><span class="band__name">Tallvane</span></div>
    <div class="contact">
      <p class="contact__name">Doran Pelliske</p>
      <p class="contact__role">PEng MBA</p>
      <p class="contact__role">President</p>
      <div class="contact__lines">
        <p>eMail: doran.pelliske@tallvane-mail.ca</p>
        <p>Phone: +14035558213</p>
      </div>
    </div>
  </section>
</main>
</body>
</html>
```